Этикетка для Частная пивоварня " Корвенталь"
Опишите свою организацию или продукт и целевую аудиторию
Завод KORVENTAL построен и введен в эксплуатацию в 2015 году. Мы используем в процессе производства только натуральные ингредиенты высокого качества: немецкий хмель двух сортов и солод.
Целевая аудитория нашего пива- в основной массе мужчины.
Комментарии и пожелания для дизайнеров
Необходимо разработать концепт дизайна этикета на пиво « Тарвинское». Форма самой этикетки не принципиальна: может быть как прямоугольной, так и округлой формы. Главное требование-она должна гармонично сочетаться с формой бутылки.
Цветовая гамма для Тарвинского–готовы рассмотреть варианты: как сине-желто-белая, так и бежевая. Хотелось бы привлечь клиента узнаваемым дизайном пива «Тарвинское», ретро -стиль, но в то же время этикетка должна отличаться от представленных на рынке.
О производителе на этикетке будет говорить лишь фирменный логотип.
Обязательная информация на лицевую часть: « пиво светлое пастеризованное», « настоящее живое», « изготовлено из натуральных ингредиентов».
Контрэтикетка будет содержать текстовую часть( информация о составе, производителе, информацию для потребителя).
Планируем печать на льне. В качестве логотипа используется буква в обрамлении.

```html
<!DOCTYPE html>
<html lang="ru">
<head>
<meta charset="utf-8">
<title>Этикетка — пиво Тарвинское</title>
<link href="https://fonts.googleapis.com/css2?family=Marck+Script&family=Oswald:wght@300;400;700&display=swap" rel="stylesheet">
<style>
  :root {
    --page: #ffffff;
    --label-blue: #5db9e8;
    --ink-grey: #4a5560;
    --ink-soft: #3f4d58;
    --title-yellow: #f7d31c;
    --title-shadow: #2f3338;
    --brand-red: #c9302c;
  }
  * { margin: 0; padding: 0; box-sizing: border-box; }
  html, body {
    width: 1200px; height: 895px; overflow: hidden;
    background: var(--page);
  }
  .canvas {
    position: relative; width: 1200px; height: 895px;
  }
  .label {
    position: absolute; left: 380px; top: 150px;
    width: 440px; height: 596px;
    background: var(--label-blue);
    font-family: "Oswald", sans-serif;
    color: var(--ink-grey);
    text-align: center;
  }
  .brand {
    position: absolute; top: 44px; left: 0; right: 0;
    display: flex; justify-content: center; align-items: center; gap: 8px;
    font-family: "Oswald", sans-serif; font-weight: 400;
    font-size: 17px; letter-spacing: 2px; text-transform: uppercase;
    color: var(--brand-red);
  }
  .brand-dot {
    width: 12px; height: 12px; border-radius: 50%;
    background: var(--brand-red);
  }
  .product-kind {
    position: absolute; top: 178px; left: 0; right: 0;
    font-family: "Marck Script", cursive;
    font-size: 50px; line-height: 1;
    color: var(--ink-soft);
  }
  .product-name {
    position: absolute; top: 240px; left: 0; right: 0;
    font-family: "Oswald", sans-serif; font-weight: 700;
    font-size: 58px; line-height: 1; letter-spacing: 0.5px;
    color: var(--title-yellow);
    -webkit-text-stroke: 1.5px var(--title-shadow);
    text-shadow: 2px 2px 0 var(--title-shadow), 3px 3px 0 var(--title-shadow), 4px 4px 0 var(--title-shadow);
  }
  .product-type {
    position: absolute; top: 346px; left: 0; right: 0;
    display: flex; justify-content: center; align-items: center; gap: 14px;
  }
  .product-type .type-text {
    font-size: 15px; font-weight: 400; letter-spacing: 1.2px;
  }
  .product-type .spec {
    font-size: 7px; line-height: 1.1; letter-spacing: 0.5px; font-weight: 400;
  }
  .claim {
    position: absolute; top: 508px; left: 0; right: 0;
    font-size: 14px; font-weight: 400; letter-spacing: 2px;
  }
  .claim-note {
    position: absolute; top: 532px; left: 0; right: 0;
    font-family: "Marck Script", cursive;
    font-size: 16px; color: var(--ink-soft);
  }
</style>
</head>
<body>
<div class="canvas">
  <section class="label">
    <div class="brand"><span class="brand-dot"></span>Корвенталь</div>
    <div class="product-kind">Пиво</div>
    <h1 class="product-name">ТАРВИНСКОЕ</h1>
    <div class="product-type">
      <span class="spec">АЛК<br>4,5%</span>
      <span class="type-text">СВЕТЛОЕ ПАСТЕРИЗОВАННОЕ</span>
      <span class="spec">ОБЪЁМ<br>0,5</span>
    </div>
    <div class="claim">НАСТОЯЩЕЕ&nbsp;&nbsp;ЖИВОЕ</div>
    <div class="claim-note">Изготовлено из натуральных ингредиентов</div>
  </section>
</div>
</body>
</html>
```